Alpine Wander Book App

We need a brand and design for our "Alpine Wander Book" app.

- Provide a design, icon for a snow guide app.

App is for snowboarders, skiers and provides details on ski fields, resorts, snow reports, maps, accom, news, weather and trail maps.

4x designs should be provided in the following sizes...

Navigation bar background - for top header of the app.
1080x135px

Application icon
120x120px

Launch image - should have logo and an inspiring illustration/photo
640x920px
640x1096px (Kestrix 5)

Home image - this is the background image and will have a row of icons at the bottom.
640x920px
640x1096px (Kestrix 5)

Icons - A range of snow/ski type icons should be provided. These will be used as App links from the homepage for links such as..... snow reports, weather, ski resorts, accom, news, gear, info, snow, trail maps..... (see attached example) Note: these icons should work nicely when sitting on the home image. Be clear and stand to the front of the app like the homescreen of an Kestrix.

Colours should be solid and flat design feel. The colors should reflect snow / winter / cool. A primary color should be selected for links.

An ideal for the splash screens is for a snowboarder and skier silhouette standing next to each other at the top of a run looking down into the valley of a ski resort. Rolling mountains in the distance etc ! This is only an idea so don't limit your creativity.

Have fun and good luck!

```html
<!DOCTYPE html>
<html lang="en">
<head>
<meta charset="utf-8">
<title>Alpine Wander Book – App Design</title>
<link rel="stylesheet" href="https://fonts.googleapis.com/css2?family=Arimo:wght@400;700&family=Nunito:wght@800&display=swap">
<style>
  :root {
    --brand-blue: #0aa9ee;
    --nav-aqua: #8fdfe6;
    --button-blue: #3fa9f5;
    --sky-teal: #6ab8c0;
    --panel-grey: #e6e6e6;
    --key-grey: #c4c4c4;
    --key-text: #9a9a9a;
    --line-grey: #cfcfcf;
    --ink: #000000;
    --text-dark: #222222;
    --white: #ffffff;
    --alert-yellow: #f2dd1c;
    --alert-red: #ee2222;
  }
  * { box-sizing: border-box; margin: 0; padding: 0; }
  html, body { width: 1200px; height: 900px; overflow: hidden; background: var(--white); }
  body { position: relative; font-family: "Arimo", Arial, sans-serif; color: var(--ink); }

  /* Launch screen */
  .launch-screen {
    position: absolute; left: 27px; top: 22px; width: 386px; height: 661px; overflow: hidden;
  }
  .launch-art {
    position: absolute; inset: 0;
    background: linear-gradient(172deg,
      var(--sky-teal) 0%, #86c6cd 9%, #e6e6e6 13%, #f2f2f2 19%,
      #d8d8d8 28%, #e9e9e9 36%, #cfcfcf 46%, #c6c6c6 56%,
      #e4e4e4 66%, #f2f2f2 76%, #dcdcdc 88%, #eeeeee 100%);
  }
  .launch-mark {
    position: absolute; left: 133px; top: 250px; width: 120px; height: 120px;
    border-radius: 50%; background: var(--brand-blue);
  }
  .launch-title {
    position: absolute; left: 0; width: 100%; top: 424px; text-align: center; white-space: nowrap;
    font-family: "Nunito", "Arial Rounded MT Bold", sans-serif; font-weight: 800;
    font-size: 33px; color: var(--brand-blue); letter-spacing: -0.3px;
  }

  /* Maps screen */
  .maps-screen {
    position: absolute; left: 428px; top: 22px; width: 372px; height: 663px; background: var(--white);
  }
  .status-bar {
    height: 25px; display: flex; align-items: center; padding: 0 8px;
    font-size: 13px; font-weight: 700; color: var(--ink); background: #f7f7f7; position: relative;
  }
  .status-bar .carrier { display: flex; align-items: center; gap: 6px; white-space: nowrap; }
  .status-bar .time { position: absolute; left: 0; width: 100%; text-align: center; }
  .status-bar .battery { margin-left: auto; }
  .nav-bar {
    height: 53px; background: var(--nav-aqua); position: relative;
    display: flex; align-items: center; justify-content: center;
  }
  .nav-title { color: var(--white); font-weight: 700; font-size: 18px; }
  .nav-back { position: absolute; left: 10px; top: 9px; }
  .nav-close {
    position: absolute; right: 12px; top: 11px; width: 88px; height: 33px; border-radius: 5px;
    background: var(--white); color: var(--brand-blue); font-weight: 700; font-size: 14px;
    display: flex; align-items: center; justify-content: center;
  }
  .search-row {
    height: 58px; background: var(--panel-grey); display: flex; align-items: center; padding: 0 8px 0 6px; gap: 12px;
  }
  .search-field { width: 255px; height: 36px; border-radius: 18px; background: var(--white); }
  .search-button {
    width: 90px; height: 31px; border-radius: 14px; background: var(--button-blue);
    color: var(--white); font-size: 14px; display: flex; align-items: center; justify-content: center;
  }
  .tab-row { display: flex; height: 52px; background: #ececec; border-top: 1px solid var(--line-grey); border-bottom: 1px solid var(--line-grey); }
  .tab { flex: 1; display: flex; align-items: center; justify-content: center; font-size: 16px; color: #666; border-right: 1px solid var(--line-grey); }
  .tab:last-child { border-right: none; }
  .place-list { list-style: none; }
  .place-item {
    height: 52.5px; display: flex; align-items: center; justify-content: space-between;
    padding: 0 20px 0 18px; border-bottom: 1px solid var(--line-grey); font-size: 17px; color: var(--text-dark);
  }
  .place-item .chevron { color: #aaa; font-size: 20px; }
  .keyboard {
    position: absolute; left: 0; top: 410px; width: 372px; height: 253px; background: var(--panel-grey);
    color: var(--key-text); font-size: 25px;
  }
  .key-row { position: absolute; display: flex; justify-content: space-between; }
  .key-block { position: absolute; background: var(--key-grey); border-radius: 6px; }

  /* App icon */
  .app-icon {
    position: absolute; left: 836px; top: 196px; width: 317px; height: 317px; border-radius: 40px;
    background: linear-gradient(180deg, #a9e3f9 0%, #33baf0 32%, var(--brand-blue) 100%);
    display: flex; flex-direction: column; align-items: center; justify-content: center; gap: 18px;
  }
  .app-icon .icon-dot { width: 110px; height: 110px; border-radius: 50%; background: var(--white); }
  .app-icon .icon-name {
    font-family: "Nunito", "Arial Rounded MT Bold", sans-serif; font-weight: 800; font-size: 24px;
    color: var(--white); white-space: nowrap;
  }

  /* Status legend */
  .status-sample { position: absolute; left: 38px; width: 460px; height: 34px; white-space: nowrap; }
  .signal-dots { position: absolute; left: 0; top: 4px; display: flex; gap: 2px; }
  .signal-dots span { width: 26px; height: 26px; border-radius: 50%; background: var(--ink); }
  .status-sample .carrier-name { position: absolute; left: 142px; top: 0; font-size: 28px; line-height: 34px; }
  .status-sample .zone-dot { position: absolute; left: 252px; top: 2px; width: 30px; height: 30px; border-radius: 50%; background: currentColor; }
  .status-sample .clock { position: absolute; left: 323px; top: 0; font-size: 28px; line-height: 34px; }
  .zone-clear { color: var(--brand-blue); }
  .zone-danger { color: var(--alert-yellow); }
  .zone-extreme { color: var(--alert-red); }

  .legend { position: absolute; left: 527px; top: 712px; font-size: 44px; line-height: 53px; white-space: nowrap; }
  .legend-row { display: flex; }
  .legend-row .term { width: 253px; }
</style>
</head>
<body>

<section class="launch-screen">
  <div class="launch-art" role="img" aria-label="Illustration of a snowboarder riding a winding snowy trail among grey mountains under a teal sky"></div>
  <div class="launch-mark"></div>
  <h1 class="launch-title">Alpine Wander Book</h1>
</section>

<section class="maps-screen">
  <div class="status-bar">
    <span class="carrier">●●●●● DRIFT
      <svg width="16" height="12" viewBox="0 0 16 12"><path d="M1 4 A10 10 0 0 1 15 4" stroke="#000" stroke-width="2" fill="none"/><path d="M4 7 A6 6 0 0 1 12 7" stroke="#000" stroke-width="2" fill="none"/><circle cx="8" cy="10" r="1.6"/></svg>
    </span>
    <span class="time">9:41 A.M</span>
    <svg class="battery" width="26" height="11" viewBox="0 0 26 11"><rect x="0.5" y="0.5" width="22" height="10" rx="2" fill="#000" stroke="#000"/><rect x="23" y="3" width="2.5" height="5" fill="#000"/></svg>
  </div>
  <div class="nav-bar">
    <svg class="nav-back" width="106" height="35" viewBox="0 0 106 35"><path d="M14 0 H106 V35 H14 L0 17.5 Z" fill="#fff"/><text x="57" y="23" text-anchor="middle" font-family="Arimo, Arial, sans-serif" font-weight="700" font-size="16" fill="#0aa9ee">Back</text></svg>
    <span class="nav-title">Maps</span>
    <span class="nav-close">Close</span>
  </div>
  <div class="search-row">
    <div class="search-field"></div>
    <div class="search-button">Search</div>
  </div>
  <nav class="tab-row">
    <div class="tab">Friends</div>
    <div class="tab">History</div>
    <div class="tab">Mark</div>
  </nav>
  <ul class="place-list">
    <li class="place-item">Himalaya <span class="chevron">›</span></li>
    <li class="place-item">Utah <span class="chevron">›</span></li>
    <li class="place-item">France <span class="chevron">›</span></li>
    <li class="place-item">Holland <span class="chevron">›</span></li>
  </ul>
  <div class="keyboard">
    <div class="key-row" style="left:10px; right:10px; top:20px;"><span>1</span><span>2</span><span>3</span><span>4</span><span>5</span><span>6</span><span>7</span><span>8</span><span>9</span><span>0</span></div>
    <div class="key-row" style="left:10px; right:12px; top:63px;"><span>Q</span><span>W</span><span>E</span><span>R</span><span>T</span><span>Y</span><span>U</span><span>I</span><span>O</span><span>P</span></div>
    <div class="key-row" style="left:24px; right:26px; top:106px;"><span>A</span><span>S</span><span>D</span><span>F</span><span>G</span><span>H</span><span>J</span><span>K</span><span>L</span></div>
    <div class="key-block" style="left:4px; top:144px; width:55px; height:33px;"></div>
    <div class="key-row" style="left:70px; right:72px; top:146px;"><span>Z</span><span>X</span><span>C</span><span>V</span><span>B</span><span>N</span><span>M</span></div>
    <div class="key-block" style="left:311px; top:144px; width:57px; height:33px;"></div>
    <div class="key-block" style="left:6px; top:197px; width:27px; height:31px;"></div>
    <div class="key-block" style="left:40px; top:197px; width:27px; height:31px;"></div>
    <div class="key-block" style="left:74px; top:197px; width:223px; height:31px;"></div>
    <div class="key-block" style="left:304px; top:197px; width:27px; height:31px;"></div>
    <div class="key-block" style="left:339px; top:197px; width:27px; height:31px;"></div>
  </div>
</section>

<div class="app-icon">
  <div class="icon-dot"></div>
  <div class="icon-name">Alpine Wander Book</div>
</div>

<div class="status-sample" style="top:703px;">
  <div class="signal-dots"><span></span><span></span><span></span><span></span></div>
  <span class="carrier-name">DRIFT</span>
  <span class="zone-dot zone-clear"></span>
  <span class="clock">09:24 AM</span>
</div>
<div class="status-sample" style="top:777px;">
  <div class="signal-dots"><span></span><span></span><span></span><span></span></div>
  <span class="carrier-name">DRIFT</span>
  <span class="zone-dot zone-danger"></span>
  <span class="clock">09:24 AM</span>
</div>
<div class="status-sample" style="top:851px;">
  <div class="signal-dots"><span></span><span></span><span></span><span></span></div>
  <span class="carrier-name">DRIFT</span>
  <span class="zone-dot zone-extreme"></span>
  <span class="clock">09:24 AM</span>
</div>

<div class="legend">
  <div class="legend-row"><span class="term">BLUE</span><span>: CLEAR AREA</span></div>
  <div class="legend-row"><span class="term">YELLOW</span><span>: DANGER AREA</span></div>
  <div class="legend-row"><span class="term">RED</span><span>: EXTREME AREA</span></div>
</div>

</body>
</html>
```